Camp Maplebrook 2019 Summer Camp Postcard

We are a Christian summer camp offering nine weeks of day camp and two weeks of overnight camp. We need a bright, colorful design that showcases our offered activities such as boating, rock wall, crafts, sports, rock wall. We want our photos highlighted/enhanced. Our colors are red, orange, brown and black.

Target Market(s)

Parents of elementary age children

Industry/Entity Type

Christian

Font styles to use
Sans Serif

Colors
fbee3d
fece3e
ffc214
ec1f27
f04a50
f37122
f78f20
333333
faa54b

Requirements
Must have
• Must Have:
• Day Camp 2019
• June 24 - August 23
• $135 per week
• Mon-Fri 8 am to 4 pm. Open to kids entering grades 1 to 8. Day camp is chock full of activities like swimming, rock wall, archery, sports, crafts, air rifles and much more! Daily lunch and snack included. Before and after-care available at an extra rate.
• Register and pay in full by April 1st, save $270!
• Overnight Camp 2018
• July 14-20 and July 21-27
• $330 per week
• Open to kids ages 8 to 14. Spend the week making new friends, sleeping in cabins, climbing the rock wall and swimming at the beach! Our guest speakers will lead twice daily chapel sessions that will challenge campers to grow in their faith.
• 42 Cedar Gate Rd. Barrington, NH 03825
• 603-555-0148
• www.maplebrook.org
Nice to have
• Bright and colorful
• Photos of happy campers participating in our listed activities

```html
<!DOCTYPE html>
<html lang="en">
<head>
<meta charset="utf-8">
<title>Camp Maplebrook – Summer Camp 2019 Postcard</title>
<link rel="stylesheet" href="https://fonts.googleapis.com/css2?family=Lilita+One&family=Arimo:ital,wght@0,400;0,700;1,700&display=swap">
<style>
  :root{
    --lemon:#fbee3d;
    --sun:#fece3e;
    --gold:#ffc214;
    --red:#ec1f27;
    --coral:#f04a50;
    --orange:#f37122;
    --tangerine:#f78f20;
    --peach:#faa54b;
    --ink:#333333;
    --paper:#e9e9e7;
    --white:#ffffff;
  }
  *{box-sizing:border-box;margin:0;padding:0}
  html,body{width:1200px;height:2835px;overflow:hidden}
  body{background:var(--paper);position:relative;font-family:"Arimo",Arial,sans-serif}
  .postcard{position:absolute;left:48px;width:1104px;height:790px;overflow:hidden;box-shadow:0 6px 18px rgba(0,0,0,.18)}
  .postcard--front{top:578px}
  .postcard--back{top:1468px;background:var(--white)}
  .postcard svg{position:absolute;inset:0;display:block}
  .display{font-family:"Lilita One","Arial Black",sans-serif}

  /* back panel text */
  .info{position:absolute;left:0;top:96px;width:500px;text-align:right;color:var(--ink);font-size:21px;line-height:27px}
  .info__title{font-family:"Lilita One","Arial Black",sans-serif;font-weight:400;font-size:33px;line-height:35px;color:var(--white);
    -webkit-text-stroke:5px var(--orange);paint-order:stroke fill;letter-spacing:1px}
  .info__key{color:var(--red);font-weight:700}
  .info__promo{font-weight:700;font-style:italic}
  .info__block + .info__block{margin-top:14px}

  .address{position:absolute;left:567px;top:28px;color:var(--ink);font-size:21px;line-height:25px;font-style:normal}
  .brand{display:flex;align-items:center;gap:10px;margin-bottom:16px}
  .brand__dot{width:22px;height:22px;border-radius:50%;background:var(--red);flex:none}
  .brand__name{font-family:"Arimo",Arial,sans-serif;font-weight:700;font-size:27px;color:var(--red);line-height:1}
</style>
</head>
<body>

<!-- FRONT -->
<section class="postcard postcard--front" aria-label="Postcard front">
  <svg viewBox="0 0 1104 790" width="1104" height="790" xmlns="http://www.w3.org/2000/svg">
    <defs>
      <linearGradient id="frontBg" x1="0" y1="0" x2="1" y2="1">
        <stop offset="0" stop-color="#f37122"/>
        <stop offset=".45" stop-color="#ffc214"/>
        <stop offset="1" stop-color="#fbee3d"/>
      </linearGradient>
      <linearGradient id="fireTone" x1="0" y1="0" x2="0.4" y2="1">
        <stop offset="0" stop-color="#f78f20"/>
        <stop offset=".4" stop-color="#c7351b"/>
        <stop offset=".75" stop-color="#7a2410"/>
        <stop offset="1" stop-color="#3a140a"/>
      </linearGradient>
      <linearGradient id="photoTone" x1="0" y1="0" x2="1" y2="0">
        <stop offset="0" stop-color="#6f8f9e"/>
        <stop offset=".2" stop-color="#e2b9a0"/>
        <stop offset=".4" stop-color="#c9554c"/>
        <stop offset=".6" stop-color="#7aa05a"/>
        <stop offset=".8" stop-color="#d9a040"/>
        <stop offset="1" stop-color="#5b7d4a"/>
      </linearGradient>
    </defs>

    <rect width="1104" height="790" fill="url(#frontBg)"/>
    <polygon points="0,0 690,0 560,790 0,790" fill="url(#fireTone)" role="img" aria-label="Photo of a large blazing campfire"/>

    <g class="stripes" fill="none" stroke="#fff" stroke-width="8">
      <line x1="712" y1="-10" x2="580" y2="800"/>
      <line x1="742" y1="-10" x2="610" y2="800"/>
      <line x1="772" y1="-10" x2="640" y2="800"/>
    </g>

    <g class="headline display" role="img" aria-label="Headline letters filled with photos of campers boating, kayaking, doing crafts and playing sports">
      <g stroke-linejoin="round">
        <text x="52" y="232" font-size="290" textLength="1000" lengthAdjust="spacingAndGlyphs" fill="none" stroke="#fff" stroke-width="26">SUMMER</text>
        <text x="52" y="232" font-size="290" textLength="1000" lengthAdjust="spacingAndGlyphs" fill="url(#photoTone)" stroke="#111" stroke-width="12" paint-order="stroke">SUMMER</text>
        <text x="528" y="440" font-size="250" textLength="505" lengthAdjust="spacingAndGlyphs" fill="none" stroke="#fff" stroke-width="26">CAMP</text>
        <text x="528" y="440" font-size="250" textLength="505" lengthAdjust="spacingAndGlyphs" fill="url(#photoTone)" stroke="#111" stroke-width="12" paint-order="stroke">CAMP</text>
      </g>
    </g>

    <g class="year display" stroke-linejoin="round">
      <text x="582" y="684" font-size="320" textLength="470" lengthAdjust="spacingAndGlyphs" fill="none" stroke="#fff" stroke-width="24">2019</text>
      <text x="582" y="684" font-size="320" textLength="470" lengthAdjust="spacingAndGlyphs" fill="#ec1f27" stroke="#111" stroke-width="10" paint-order="stroke">2019</text>
    </g>

    <text class="tagline display" x="48" y="742" font-size="50" textLength="800" lengthAdjust="spacingAndGlyphs"
          fill="#fff" stroke="#333" stroke-width="8" stroke-linejoin="round" paint-order="stroke">CHRISTIAN CAMPING SINCE 1952</text>

    <g class="brand-mark">
      <circle cx="890" cy="724" r="11" fill="#ec1f27"/>
      <text x="910" y="718" font-family="Arimo, Arial, sans-serif" font-weight="700" font-size="26" fill="#ec1f27">Camp</text>
      <text x="910" y="746" font-family="Arimo, Arial, sans-serif" font-weight="700" font-size="26" fill="#ec1f27">Maplebrook</text>
    </g>
  </svg>
</section>

<!-- BACK -->
<section class="postcard postcard--back" aria-label="Postcard back">
  <svg viewBox="0 0 1104 790" width="1104" height="790" xmlns="http://www.w3.org/2000/svg">
    <defs>
      <linearGradient id="panelBg" x1="0" y1="0" x2="0" y2="1">
        <stop offset="0" stop-color="#f78f20"/>
        <stop offset=".5" stop-color="#ffc214"/>
        <stop offset="1" stop-color="#fece3e"/>
      </linearGradient>
      <linearGradient id="lakeTone" x1="0" y1="0" x2="1" y2="0">
        <stop offset="0" stop-color="#4e5a3e"/>
        <stop offset=".5" stop-color="#8a8f8a"/>
        <stop offset="1" stop-color="#c07a2e"/>
      </linearGradient>
      <linearGradient id="flameTone" x1="0" y1="0" x2="0" y2="1">
        <stop offset="0" stop-color="#f04a50"/>
        <stop offset=".6" stop-color="#ec1f27"/>
        <stop offset="1" stop-color="#8a4a22"/>
      </linearGradient>
    </defs>

    <rect x="0" y="0" width="530" height="790" fill="url(#panelBg)"/>
    <polygon points="0,0 530,0 530,70 0,190" fill="url(#lakeTone)" role="img" aria-label="Photo of a lakeside cross with autumn trees"/>
    <g fill="none" stroke="#fff" stroke-width="6">
      <line x1="0" y1="205" x2="530" y2="85"/>
      <line x1="0" y1="225" x2="530" y2="105"/>
      <line x1="0" y1="245" x2="530" y2="125"/>
    </g>
    <g fill="none" stroke="#fbee3d" stroke-width="5">
      <line x1="528" y1="0" x2="528" y2="790"/>
      <line x1="540" y1="0" x2="540" y2="790"/>
      <line x1="552" y1="0" x2="552" y2="790"/>
    </g>
    <path d="M20,300 C140,330 200,440 170,560 C150,620 80,650 20,640 Z" fill="url(#flameTone)" role="img" aria-label="Illustration of a campfire with logs"/>
  </svg>

  <div class="info">
    <div class="info__block">
      <h2 class="info__title">DAY<br>CAMP</h2>
      <p class="info__key">June 24 - August 23<br>$135 per week<br>Mon-Fri 8 am to 4 pm.<br>Open to kids entering grades 1 to 8.</p>
      <p>Day camp is chock full of activities like<br>swimming, rock wall, archery, sports,<br>crafts, air rifles and much more!<br>Daily lunch and snack included.<br>Before and after-care<br>available at an extra rate.</p>
      <p class="info__promo">Register and pay in full<br>by April 1st, save $270!</p>
    </div>
    <div class="info__block">
      <h2 class="info__title">OVERNIGHT CAMP</h2>
      <p class="info__key">July 14-20 &amp; July 21-27<br>$330 per week<br>Open to kids ages 8 to 14.</p>
      <p>Spend the week making new friends,<br>sleeping in cabins, climbing the rock wall and<br>swimming at the beach! Our guest speakers<br>will lead twice daily chapel sessions that will<br>challenge campers to grow in their faith.</p>
    </div>
  </div>

  <address class="address">
    <div class="brand"><span class="brand__dot"></span><span class="brand__name">Camp Maplebrook</span></div>
    42 Cedar Gate Rd.<br>Barrington, NH 03825<br>603-555-0148<br>www.maplebrook.org
  </address>
</section>

</body>
</html>
```